Business Cards and Logo

KMR - Personal Injury Attorneys is the name of the firm.
We are personal injury lawyers. We want a crisp, modern and impactful design.
Color schemes are white, matte black and light grey OR white, matte black and red OR white, matte black and a nice blue or yellow.
For logo - we don’t want typical logos like scales of justice or a hammer. We want a general design with the KMR letters.
Target Market(s)
People who need attorneys.
Industry/Entity Type
Law Firm
Contact Information for Business Card
Back side: text: Harlow Bay - Brookvale - Westmere - Crestford
Front side
Name of firm and logo.
Tomas Velquist
712 W. Harlow Ave. 4th Floor
Brookvale, CA 90000
(555)014-2736 (c)
(555)019-6521 (o)
Tomas@counselwestex.com
Logo Text
KMR
Font styles to use
Other font styles liked:
- Musk - regular. Military - regular. Moonglade. Future. Or similar fonts.
Requirements
Must have
- See above. Nothing else to provide.
- KMR - Personal Injury Attorneys is the name of the firm.
- We are personal injury lawyers. We want a crisp, modern and impactful design.
- Color schemes are white, matte black and light grey OR white, matte black and red OR white, matte black and a nice blue or yellow.
- For logo - we don’t want typical logos like scales of justice or a hammer. We want a general design with the KMR letters.
Nice to have
- See above - nothing else to provide.
Should not have

```html
<!DOCTYPE html>
<html lang="en">
<head>
<meta charset="utf-8">
<title>KMR Personal Injury Attorneys – Business Cards</title>
<link href="https://fonts.googleapis.com/css2?family=Barlow:wght@300;400;600;700&family=Barlow+Semi+Condensed:wght@600;700&display=swap" rel="stylesheet">
<style>
  :root {
    --stage: #2b2d30;
    --paper: #ffffff;
    --matte-black: #121212;
    --brand-blue: #2a3db0;
    --ink: #1a1a1a;
    --rule: #222222;
    --white: #ffffff;
  }
  * { box-sizing: border-box; margin: 0; padding: 0; }
  html, body { width: 1200px; height: 900px; overflow: hidden; }
  body {
    background: var(--stage);
    font-family: "Barlow", Arial, sans-serif;
    position: relative;
  }

  .card {
    position: absolute;
    width: 560px;
    height: 320px;
    overflow: hidden;
    box-shadow: 0 10px 30px rgba(0,0,0,0.45);
  }
  .card__band {
    position: absolute;
    left: 0; right: 0; bottom: 0;
    height: 20px;
    background: var(--brand-blue);
  }

  /* lockup */
  .lockup { display: flex; align-items: center; white-space: nowrap; }
  .lockup__mark {
    font-family: "Barlow Semi Condensed", Arial, sans-serif;
    font-weight: 700;
    letter-spacing: 1px;
    line-height: 1;
  }
  .lockup__divider {
    width: 2px;
    align-self: stretch;
  }
  .lockup__words {
    font-family: "Barlow Semi Condensed", Arial, sans-serif;
    font-weight: 700;
    text-transform: uppercase;
    line-height: 1.0;
  }

  /* front */
  .card--front { left: 580px; top: 50px; background: var(--paper); color: var(--ink); }
  .card--front .lockup { position: absolute; left: 34px; top: 30px; }
  .card--front .lockup__mark { font-size: 50px; color: var(--brand-blue); }
  .card--front .lockup__divider { background: var(--ink); margin: 0 14px; }
  .card--front .lockup__words { font-size: 23px; color: var(--ink); }
  .card__name {
    position: absolute; left: 34px; top: 112px;
    font-size: 22px; font-weight: 700; letter-spacing: 0.3px;
  }
  .card__rule {
    position: absolute; left: 215px; right: 0; top: 128px;
    height: 1px; background: var(--rule);
  }
  .card__contacts {
    position: absolute; left: 34px; top: 150px;
    list-style: none; font-size: 14.5px; font-weight: 300; line-height: 1.45;
  }
  .card__address {
    position: absolute; right: 34px; bottom: 42px;
    font-style: normal; text-align: right;
    font-size: 16px; font-weight: 300; line-height: 1.35;
  }

  /* back */
  .card--back { left: 60px; top: 410px; background: var(--matte-black); color: var(--white); }
  .card--back .lockup { position: absolute; left: 70px; top: 100px; }
  .card--back .lockup__mark { font-size: 70px; color: var(--white); }
  .card--back .lockup__divider { background: var(--white); margin: 0 18px; }
  .card--back .lockup__words { font-size: 32px; color: var(--white); }
  .card__cities {
    position: absolute; left: 0; right: 0; bottom: 38px;
    text-align: center; font-size: 15px; font-weight: 300; letter-spacing: 0.4px;
  }

  /* standalone lockup */
  .brand-lockup { position: absolute; left: 720px; top: 785px; }
  .brand-lockup .lockup__mark { font-size: 66px; color: var(--white); }
  .brand-lockup .lockup__divider { background: var(--white); margin: 0 18px; }
  .brand-lockup .lockup__words { font-size: 33px; color: var(--white); }
</style>
</head>
<body>

  <section class="card card--front" aria-label="Business card front">
    <div class="lockup">
      <span class="lockup__mark">KMR</span>
      <span class="lockup__divider"></span>
      <span class="lockup__words">Personal<br>Injury Attorneys</span>
    </div>
    <h1 class="card__name">Tomas Velquist</h1>
    <div class="card__rule"></div>
    <ul class="card__contacts">
      <li>C: (555)014-2736</li>
      <li>O: (555)019-6521</li>
      <li>Tomas@counselwestex.com</li>
      <li>www.counselwestex.com</li>
    </ul>
    <address class="card__address">712 W. Harlow Ave.<br>4th Floor, Brookvale<br>CA 90000</address>
    <div class="card__band"></div>
  </section>

  <section class="card card--back" aria-label="Business card back">
    <div class="lockup">
      <span class="lockup__mark">KMR</span>
      <span class="lockup__divider"></span>
      <span class="lockup__words">Personal<br>Injury Attorneys</span>
    </div>
    <p class="card__cities">Harlow Bay - Brookvale - Westmere - Crestford</p>
    <div class="card__band"></div>
  </section>

  <div class="lockup brand-lockup" aria-label="KMR Personal Injury Attorneys logo">
    <span class="lockup__mark">KMR</span>
    <span class="lockup__divider"></span>
    <span class="lockup__words">Personal<br>Injury Attorneys</span>
  </div>

</body>
</html>
```